I need a label design for my up coming wine bottle

The bottle is a standard wine bottle, 720 ML. The label needs to be elegant 1-3 colors preferably with grape vines highlighting my winery name. 5-8 cellars

```html
<!DOCTYPE html>
<html lang="en">
<head>
<meta charset="utf-8">
<title>5-8 Cellars – Wine Label</title>
<link rel="stylesheet" href="https://fonts.googleapis.com/css2?family=Bodoni+Moda:wght@500&family=Oswald:wght@400;600&family=Parisienne&display=swap">
<style>
  :root {
    --page: #ffffff;
    --paper-top: #fcf7ee;
    --paper-bottom: #ede7da;
    --gold: #8a7350;
    --gold-light: #b59f78;
    --gold-pale: #e6dcc6;
    --ink: #333333;
    --white: #ffffff;
  }
  html, body {
    margin: 0;
    width: 1200px;
    height: 2400px;
    overflow: hidden;
    background: var(--page);
  }
  .canvas {
    position: relative;
    width: 1200px;
    height: 2400px;
  }
  .wine-label {
    position: absolute;
    left: 150px;
    top: 340px;
    width: 900px;
    height: 1720px;
    filter: drop-shadow(0 4px 10px rgba(0,0,0,0.12));
  }
  .brand-number, .brand-name, .product-name, .year {
    font-family: "Bodoni Moda", serif;
    font-weight: 500;
    fill: var(--ink);
  }
  .premium {
    font-family: "Oswald", sans-serif;
    font-weight: 600;
    fill: var(--white);
  }
  .edition {
    font-family: "Oswald", sans-serif;
    font-weight: 400;
    fill: var(--white);
    letter-spacing: 1px;
  }
  .since {
    font-family: "Parisienne", cursive;
    fill: var(--gold);
  }
</style>
</head>
<body>
<main class="canvas">
  <svg class="wine-label" viewBox="0 0 628 1200" xmlns="http://www.w3.org/2000/svg">
    <defs>
      <linearGradient id="paper" x1="0" y1="0" x2="0" y2="1">
        <stop offset="0" stop-color="var(--paper-top)"/>
        <stop offset="1" stop-color="var(--paper-bottom)"/>
      </linearGradient>
      <linearGradient id="goldBand" x1="0" y1="0" x2="0" y2="1">
        <stop offset="0" stop-color="#9c8562"/>
        <stop offset="1" stop-color="#7d6643"/>
      </linearGradient>
      <linearGradient id="vineTone" x1="0" y1="0" x2="0" y2="1">
        <stop offset="0" stop-color="var(--gold-pale)" stop-opacity="0.55"/>
        <stop offset="1" stop-color="var(--gold-pale)" stop-opacity="0.15"/>
      </linearGradient>
    </defs>

    <!-- label body and frame -->
    <path class="label-shape" d="M110,0 L518,0 L628,100 L628,880 A314,320 0 0 1 0,880 L0,100 Z" fill="url(#paper)"/>
    <path class="label-frame" d="M120,14 L508,14 L614,104 L614,880 A300,306 0 0 1 14,880 L14,104 Z" fill="none" stroke="var(--gold)" stroke-width="3"/>

    <!-- grape vine decoration -->
    <rect class="vine-decoration" role="img" aria-label="Faint grape vine with curling leaves climbing the right side"
          x="410" y="140" width="170" height="900" rx="60" fill="url(#vineTone)"/>

    <!-- brand name -->
    <text class="brand-number" x="325" y="295" text-anchor="middle" font-size="95">5-8</text>
    <text class="brand-name" x="320" y="412" text-anchor="middle" font-size="122">Cellars</text>

    <!-- product frame -->
    <path class="product-frame-outer" d="M90,520 L535,520 L535,535 L550,535 L550,700 L535,700 L535,715 L90,715 L90,700 L75,700 L75,535 L90,535 Z"
          fill="none" stroke="var(--gold)" stroke-width="2"/>
    <rect class="product-frame-inner" x="90" y="535" width="445" height="165" rx="14" fill="none" stroke="var(--gold)" stroke-width="6"/>
    <text class="product-name" x="316" y="655" text-anchor="middle" font-size="122">Wine</text>

    <!-- flourishes -->
    <rect class="flourish" role="img" aria-label="Curled flourish" x="45" y="735" width="125" height="42" rx="21" fill="var(--gold-pale)"/>
    <rect class="flourish" role="img" aria-label="Curled flourish" x="458" y="735" width="125" height="42" rx="21" fill="var(--gold-pale)"/>

    <!-- premium ribbon -->
    <rect class="ribbon" x="210" y="720" width="208" height="240" fill="url(#goldBand)"/>
    <text class="premium" x="314" y="800" text-anchor="middle" font-size="52" textLength="185" lengthAdjust="spacingAndGlyphs">PREMIUM</text>
    <line x1="245" y1="815" x2="383" y2="815" stroke="var(--white)" stroke-width="2"/>
    <text class="edition" x="314" y="857" text-anchor="middle" font-size="22">LIMITED EDITION</text>

    <!-- bottom ribbon -->
    <rect class="ribbon" x="210" y="1110" width="208" height="90" fill="url(#goldBand)"/>

    <!-- year medallion -->
    <ellipse cx="314" cy="1012" rx="165" ry="93" fill="var(--paper-bottom)" stroke="var(--gold)" stroke-width="3"/>
    <ellipse cx="314" cy="1016" rx="135" ry="82" fill="none" stroke="var(--gold)" stroke-width="3"/>
    <rect class="leaf-sprig" role="img" aria-label="Small leaf sprig" x="90" y="995" width="60" height="26" rx="13" fill="var(--gold-light)"/>
    <rect class="leaf-sprig" role="img" aria-label="Small leaf sprig" x="478" y="995" width="60" height="26" rx="13" fill="var(--gold-light)"/>
    <text class="since" x="292" y="992" text-anchor="middle" font-size="62">Since</text>
    <text class="year" x="338" y="1072" text-anchor="middle" font-size="78">1987</text>
  </svg>
</main>
</body>
</html>
```